Window and GutterCleaning Flyer A5 size double sided.

We need a double sided A5 flyer. Side 1, is for window cleaning, side 2 is for gutter cleaning. Licensed by Borough of Halvern Council.
Phone number 0800 315 4720.
Business address 7 Tarnlow Brae, North Pellin Edinburgh EH14 3RW.
www.clearpane-vista-services.com
We use a LoftPro Gutter inspection Cam to view your gutters first to see if they need doing.
Window cleaning ; Professional window cleaning services, what we offer, water fed pole window cleaning able to reach windows up to 60 feet.
Conservatory cleaning.
Conservatory roof cleaning.
Fascias & Soffits cleaning.
Excellent Customer Service.
Target Market(s)
domestic houses
Industry/Entity Type
window cleaning
Look and feel
Each slider illustrates characteristics of the customer's brand and the style your logo design should communicate.

```html
<!DOCTYPE html>
<html lang="en">
<head>
<meta charset="utf-8">
<title>ClearPane Vista Services – Window &amp; Gutter Cleaning Flyer</title>
<link href="https://fonts.googleapis.com/css2?family=Arimo:wght@400;700&display=swap" rel="stylesheet">
<style>
  :root {
    --navy: #2a285e;
    --sky: #9fc6ea;
    --white: #ffffff;
    --backdrop: #d3d3d3;
    --ink: #1c1c24;
  }
  * { box-sizing: border-box; margin: 0; padding: 0; }
  html, body { width: 1200px; height: 2351px; overflow: hidden; }
  body { background: var(--backdrop); font-family: "Arimo", Arial, sans-serif; position: relative; }

  .flyer { position: absolute; left: 230px; width: 741px; height: 1047px; overflow: hidden; }
  .flyer--window { top: 76px; background: var(--navy); }
  .flyer--gutter { top: 1200px; background: var(--white); }

  .photo { position: absolute; left: 0; top: 0; width: 100%; }
  .photo--window { height: 600px;
    background: linear-gradient(120deg, #c9c5c2 0%, #e6e6ea 35%, #b9bcc6 60%, #f1f2f4 100%); }
  .photo--gutter { height: 400px;
    background: radial-gradient(ellipse at 40% 75%, #a9763c 0%, #6d4a2a 40%, transparent 70%),
                linear-gradient(160deg, #3d3f45 0%, #5a5d62 40%, #8b6b3e 70%, #c48a3e 100%); }

  .wave { position: absolute; left: 0; width: 100%; }

  .brand-name { position: absolute; left: 40px; top: 50px; width: 140px;
    font-weight: 700; font-size: 26px; line-height: 1.05; color: var(--navy); }
  .brand-name--footer { left: auto; right: 36px; top: 920px; width: 130px; text-align: right; font-size: 24px; }

  .title { position: absolute; left: 0; width: 100%; text-align: center;
    font-weight: 700; color: var(--white); font-size: 104px; line-height: 1;
    letter-spacing: -1px; text-shadow: 0 4px 12px rgba(0,0,0,.45); }

  .intro { position: absolute; left: 40px; right: 40px; top: 706px; text-align: center;
    color: var(--white); font-size: 16px; line-height: 21px; }
  .intro p + p { margin-top: 18px; }

  .contact-center { position: absolute; left: 0; width: 100%; text-align: center; color: var(--white); }
  .phone-big { top: 910px; font-weight: 700; font-size: 25px; }
  .address-line { top: 941px; font-size: 16px; }
  .web-spaced { top: 978px; font-weight: 700; font-size: 15px; letter-spacing: 4px; }
  .licence { top: 1010px; font-size: 13px; opacity: .9; }

  .body-copy { position: absolute; left: 36px; right: 36px; top: 458px;
    color: var(--ink); font-size: 16px; line-height: 21px; }
  .body-copy p + p { margin-top: 19px; }

  .contact-list { position: absolute; left: 36px; top: 922px; color: var(--ink); font-size: 16px; list-style: none; }
  .contact-list li { display: flex; align-items: center; gap: 14px; height: 21px; }
  .contact-list svg { width: 12px; height: 12px; fill: var(--ink); }

  .web-bar { position: absolute; left: 0; top: 979px; width: 344px; height: 30px;
    background: var(--navy); color: var(--white); font-size: 16px;
    display: flex; align-items: center; gap: 14px; padding-left: 36px; }
  .web-bar .dot { width: 8px; height: 8px; border-radius: 50%; background: var(--white); }
</style>
</head>
<body>

<section class="flyer flyer--window">
  <div class="photo photo--window" role="img" aria-label="Photo of a window cleaner wiping tall windows with a squeegee pole"></div>
  <svg class="wave" style="top:500px" width="741" height="120" viewBox="0 0 741 120" aria-hidden="true">
    <path d="M0 40 C150 80 300 40 420 60 C540 80 650 60 741 28 L741 120 L0 120 Z" fill="#2a285e"/>
    <path d="M0 22 C150 62 300 22 420 50 C540 76 650 52 741 16" fill="none" stroke="#2a285e" stroke-width="3"/>
    <path d="M0 30 C150 70 300 30 420 54 C540 78 650 56 741 22" fill="none" stroke="#ffffff" stroke-width="2"/>
    <path d="M0 36 C150 76 300 36 420 57 C540 80 650 58 741 25" fill="none" stroke="#2a285e" stroke-width="2"/>
  </svg>
  <div class="brand-name">ClearPane Vista</div>
  <h1 class="title" style="top:462px">WINDOW</h1>
  <h1 class="title" style="top:562px">CLEANING</h1>

  <div class="intro">
    <p>We offer a high quality, professional window cleaning service across west Edinburgh.</p>
    <p>Regular window cleaning helps to avoid the build-up of dirt and residue on the glass, meaning more light can get into your home and can also improve its external appearance. Our water fed pole system reaches windows up to 60 feet. We also offer conservatory and conservatory roof cleaning, fascias &amp; soffits cleaning, gutter/rhone cleaning and painting, and builders cleans – all with excellent customer service.</p>
  </div>

  <div class="contact-center phone-big">0800 315 4720</div>
  <div class="contact-center address-line">7 Tarnlow Brae, North Pellin Edinburgh EH14 3RW</div>
  <div class="contact-center web-spaced">www.clearpane-vista-services.com</div>
  <div class="contact-center licence">Licensed by Borough of Halvern Council</div>
</section>

<section class="flyer flyer--gutter">
  <div class="photo photo--gutter" role="img" aria-label="Photo of a gloved hand clearing autumn leaves from a roof gutter"></div>
  <svg class="wave" style="top:330px" width="741" height="110" viewBox="0 0 741 110" aria-hidden="true">
    <path d="M0 40 C140 0 260 20 380 40 C520 62 640 30 741 50 L741 110 L0 110 Z" fill="#ffffff"/>
    <path d="M0 28 C140 -10 260 10 380 30 C520 52 640 20 741 40" fill="none" stroke="#ffffff" stroke-width="4"/>
    <path d="M0 34 C140 -4 260 16 380 36 C520 58 640 26 741 46" fill="none" stroke="#5a3a22" stroke-width="2"/>
    <path d="M0 46 C140 8 260 28 380 48 C520 70 640 38 741 58" fill="none" stroke="#2a285e" stroke-width="2"/>
  </svg>
  <h1 class="title" style="top:80px">GUTTER</h1>
  <h1 class="title" style="top:182px">CLEANING</h1>

  <div class="body-copy">
    <p>ClearPane Vista Services offer a fast and easy gutter cleaning service on residential and commercial properties.</p>
    <p>Gutters are an important part of your home. Letting your gutters get blocked up can cause damage to your property, so why not set up an annual plan and make sure you don’t run into problems when winter comes.</p>
    <p>Over time your gutters will fill up with moss, leaves and other unwanted debris which will affect the appearance of your home. When gutters aren’t cleared and emptied on a regular basis they become heavy and risk pulling away from the fascias.</p>
    <p>When gutters are not clear it can also lead to blockages in the gutters and downpipes, which will cause the water to overflow. The water which overflows from the guttering can lead to damp problems and other problems in the structure of your property which can become a costly repair.</p>
    <p>We use a LoftPro gutter inspection camera to view your gutters first to see if they need doing. We recommend gutters to be cleared out once a year. If they are blocked and overflowing, contact us for a free no obligation quote. We will clear all gutters and unblock all downpipes ensuring the water is running freely and down your drains.</p>
  </div>

  <ul class="contact-list">
    <li><svg viewBox="0 0 24 24"><path d="M6.6 10.8a15 15 0 0 0 6.6 6.6l2.2-2.2a1 1 0 0 1 1-.25 11.4 11.4 0 0 0 3.6.57 1 1 0 0 1 1 1V20a1 1 0 0 1-1 1A17 17 0 0 1 3 4a1 1 0 0 1 1-1h3.5a1 1 0 0 1 1 1c0 1.25.2 2.45.57 3.6a1 1 0 0 1-.25 1z"/></svg>0800 315 4720</li>
    <li><svg viewBox="0 0 24 24"><path d="M12 2a7 7 0 0 0-7 7c0 5.2 7 13 7 13s7-7.8 7-13a7 7 0 0 0-7-7zm0 9.5A2.5 2.5 0 1 1 12 6.5a2.5 2.5 0 0 1 0 5z"/></svg>7 Tarnlow Brae,&nbsp; North Pellin Edinburgh EH14 3RW</li>
  </ul>
  <div class="web-bar"><span class="dot"></span>www.clearpane-vista-services.com</div>
  <div class="brand-name brand-name--footer">ClearPane Vista</div>
</section>

</body>
</html>
```